Seeking funky, innovative business cards

I am looking to refresh our current business cards to something more engaging, visual and impactful. We are a management consultancy firm, see website (www.larkspur-advisory.com.au). I've included our colour scheme, sample of the slides we use and our old business cards. We would like our cards to have icons. The card should display:- Name- Title- Mobile number- Address- Email address- Website - Company logo- Our purpose statement "We shape workplaces where people truly thrive"

Contact Information for Business Card

Tavish Brellan
Consultant
0491 672 348
Level 5, 218 Warrick Lane, Melbourne 3000
tavish@larkspur-advisory.com.au
www.larkspur-advisory.com.au

Purpose statement "We shape workplaces where people truly thrive"
LOGO available in google images

Font styles to use
Other font styles liked:
• Open Sans Light, Bebas Neue (open to other cool foints)

Colors
ffc214
5c5c5c
f5f5f5
fefefe

Requirements
Must have
• - Name
• - Title
• - Mobile number
• - Address
• - Email address
• - Website
• - Company logo
• - Our purpose statement "We shape workplaces where people truly thrive"
Nice to have
• - Icons
• - Colour (see our colour scheme"

```html
<!DOCTYPE html>
<html lang="en">
<head>
<meta charset="utf-8">
<title>Larkspur Advisory – Business Card</title>
<link rel="stylesheet" href="https://fonts.googleapis.com/css2?family=Lato:wght@300;400;700&family=Open+Sans:wght@400&display=swap">
<style>
  :root {
    --stage: #454545;
    --orange: #e9962f;
    --orange-light: #f2aa4c;
    --orange-deep: #dd8a2a;
    --band: #f1eeeb;
    --white: #fefefe;
    --paper: #f5f5f5;
    --paper-shade: #dcdcdc;
    --ink: #5c5c5c;
  }
  * { margin: 0; padding: 0; box-sizing: border-box; }
  html, body { width: 1200px; height: 1031px; overflow: hidden; }
  body { background: var(--stage); font-family: "Lato", sans-serif; position: relative; }

  .card { position: absolute; left: 254px; width: 697px; height: 398px; overflow: hidden; }
  .card--front { top: 82px; }
  .card--back { top: 553px; }

  .card__texture { position: absolute; inset: 0; }
  .card--front .card__texture { background: linear-gradient(135deg, var(--orange-light) 0%, var(--orange) 55%, var(--orange-deep) 100%); }
  .card--back .card__texture { background: linear-gradient(135deg, var(--white) 0%, var(--paper) 45%, var(--paper-shade) 100%); }

  .wordmark { position: absolute; font-family: "Lato", sans-serif; font-weight: 300; white-space: nowrap; line-height: 1; }
  .wordmark__dot { display: inline-block; border-radius: 50%; vertical-align: middle; }

  .card--front .wordmark { left: 0; right: 0; top: 150px; text-align: center; font-size: 60px; color: var(--white); }
  .card--front .wordmark__dot { width: 12px; height: 12px; background: var(--white); margin-right: 14px; }

  .purpose-band { position: absolute; left: 0; right: 0; top: 311px; height: 24px; background: var(--band); }
  .purpose { display: block; text-align: center; font-size: 23px; line-height: 24px; color: var(--orange); text-transform: uppercase; letter-spacing: -0.3px; white-space: nowrap; }
  .website { position: absolute; left: 0; right: 0; top: 338px; text-align: center; font-family: "Open Sans", sans-serif; font-size: 21px; color: var(--white); letter-spacing: 0.5px; }

  .card--back .wordmark { left: 38px; top: 176px; font-size: 47px; color: var(--ink); }
  .card--back .wordmark__dot { width: 9px; height: 9px; background: var(--ink); margin-right: 8px; }

  .person { position: absolute; left: 296px; top: 112px; }
  .person__name { font-weight: 400; font-size: 51px; line-height: 50px; color: var(--orange); }
  .person__title { margin-top: 6px; font-size: 19.5px; letter-spacing: 1px; color: var(--ink); text-transform: uppercase; }

  .contact { position: absolute; left: 308px; top: 262px; list-style: none; font-family: "Open Sans", sans-serif; font-size: 20.5px; color: var(--ink); letter-spacing: 0.4px; }
  .contact__item { display: flex; align-items: flex-start; line-height: 26.5px; }
  .contact__icon { width: 20px; height: 20px; flex: none; margin-top: 3px; margin-right: 12px; }
</style>
</head>
<body>

<section class="card card--front" aria-label="Card front">
  <div class="card__texture" role="img" aria-label="Orange gradient with a faint network pattern of joined dots"></div>
  <div class="wordmark"><span class="wordmark__dot"></span>Larkspur</div>
  <div class="purpose-band"><span class="purpose">We shape workplaces where people truly thrive</span></div>
  <div class="website">www.larkspur-advisory.com.au</div>
</section>

<section class="card card--back" aria-label="Card back">
  <div class="card__texture" role="img" aria-label="Light grey gradient with a faint network pattern of joined dots"></div>
  <div class="wordmark"><span class="wordmark__dot"></span>Larkspur</div>

  <div class="person">
    <h1 class="person__name">Tavish<br>Brellan</h1>
    <p class="person__title">Consultant</p>
  </div>

  <ul class="contact">
    <li class="contact__item">
      <svg class="contact__icon" viewBox="0 0 20 20" aria-hidden="true"><circle cx="10" cy="10" r="10" fill="#5c5c5c"/><rect x="6.5" y="4.5" width="7" height="11" rx="1.2" fill="none" stroke="#fefefe" stroke-width="1.5"/><circle cx="10" cy="13.3" r="0.9" fill="#fefefe"/></svg>
      <span>0491 672 348</span>
    </li>
    <li class="contact__item">
      <svg class="contact__icon" viewBox="0 0 20 20" aria-hidden="true"><circle cx="10" cy="10" r="10" fill="#5c5c5c"/><path d="M10 4.5a4 4 0 0 0-4 4c0 3 4 7 4 7s4-4 4-7a4 4 0 0 0-4-4z" fill="#fefefe"/><circle cx="10" cy="8.5" r="1.6" fill="#5c5c5c"/></svg>
      <span>Level 5, 218 Warrick Lane,<br>Melbourne 3000</span>
    </li>
    <li class="contact__item">
      <svg class="contact__icon" viewBox="0 0 20 20" aria-hidden="true"><circle cx="10" cy="10" r="10" fill="#5c5c5c"/><rect x="5" y="6.5" width="10" height="7.5" rx="0.8" fill="none" stroke="#fefefe" stroke-width="1.4"/><path d="M5.3 7l4.7 3.8L14.7 7" fill="none" stroke="#fefefe" stroke-width="1.4"/></svg>
      <span>tavish@larkspur-advisory.com.au</span>
    </li>
  </ul>
</section>

</body>
</html>
```